Life Coaching Business - needs business card design with logo

I need a business card and logo design for a life coaching business I started based in Los Angeles. I offer services to clients that wish to bring more balance and overall wholeness to their lives. As of right now, the business name is "Marcus Elwood Coaching." An iidea I had for the logo was to be kind of a Yin-Yang symbol but with dolphins, as the dolphin has symbolic meaning for my business. Although I am really open to other ideas as long as it incorporates the idea of “balance,” “wholeness,” and “dolphins.”I also wanted to incorporate the color blue, maybe in the form of water, waves, or some sort of peaceful imagery.

```html
<!DOCTYPE html>
<html lang="en">
<head>
<meta charset="utf-8">
<title>Marcus Elwood Coaching – Business Card</title>
<link href="https://fonts.googleapis.com/css2?family=Open+Sans:wght@400;600&display=swap" rel="stylesheet">
<style>
  :root {
    --paper: #e6e6e6;
    --card: #0d0d0d;
    --ink: #f2f2f2;
    --ink-soft: #d6d6d6;
    --mark: #f4f4f4;
  }
  html, body {
    margin: 0;
    padding: 0;
    width: 1200px;
    height: 800px;
    overflow: hidden;
    background: var(--paper);
    font-family: "Open Sans", Arial, sans-serif;
  }
  .sheet {
    width: 1200px;
    height: 800px;
    display: flex;
    flex-direction: column;
    align-items: center;
    justify-content: center;
    gap: 48px;
  }
  .card {
    width: 560px;
    height: 320px;
    background: var(--card);
    color: var(--ink);
    border-radius: 4px;
    box-sizing: border-box;
    box-shadow: 0 6px 18px rgba(0,0,0,0.18);
    display: flex;
    align-items: center;
  }
  .card-front {
    padding: 0 48px;
    gap: 40px;
  }
  .brand-circle {
    flex: none;
    border-radius: 50%;
    background: var(--mark);
  }
  .card-front .brand-circle {
    width: 200px;
    height: 200px;
  }
  .front-name {
    margin: 0;
    font-weight: 400;
    font-size: 38px;
    line-height: 1.2;
    letter-spacing: 0.3px;
  }
  .card-back {
    padding: 0 48px;
    gap: 36px;
  }
  .card-back .brand-circle {
    width: 120px;
    height: 120px;
  }
  .back-info {
    display: flex;
    flex-direction: column;
  }
  .back-name {
    margin: 0 0 22px;
    font-weight: 400;
    font-size: 24px;
    letter-spacing: 0.3px;
  }
  .contact-list {
    list-style: none;
    margin: 0;
    padding: 0;
    font-size: 17px;
    line-height: 1.6;
    color: var(--ink-soft);
    letter-spacing: 0.5px;
  }
</style>
</head>
<body>
  <main class="sheet">
    <section class="card card-front" aria-label="Card front">
      <div class="brand-circle" aria-hidden="true"></div>
      <h1 class="front-name">Marcus Elwood<br>Coaching</h1>
    </section>

    <section class="card card-back" aria-label="Card back">
      <div class="brand-circle" aria-hidden="true"></div>
      <div class="back-info">
        <h2 class="back-name">Marcus Elwood Coaching</h2>
        <ul class="contact-list">
          <li>Mob. xxxxxxxxxxx</li>
          <li>E-mail xxxxxxxxxxx</li>
          <li>adress: xxxxxxxxxx</li>
          <li>www.xxxxxxxx.com</li>
        </ul>
      </div>
    </section>
  </main>
</body>
</html>
```